BRDQ "Poo" Cartoon Illustrations

BRDQ are creating a Facebook campaign (1200px x 628px).
It was be useful if the image was suitable for 1:1 ratio as well.
The image/Illustration is to cartoonist/comical in nature. Have some colours.

The company “BRDQ” services Septic Tanks (tanks that store/manage human sewage.
We want to put some fun into the topic, and use characters that look like turds ‘Human Feces’
We have included a cartoon character from the web “please note this is for reference only and may have copyright.

We have 3 ideas;
Poo's running a foot race through a finishing line "BRDQ Logo" .Caption "Keep your septic in tip top condition - Call BRDQ to arrange a servic

A fun water slide with the Poo's coming down and launching into the Septic Tank.
Caption: Service Your Septic and let the fun begin.

Another: Poos in a lazy setting, in a Septic tank.
Caption: Get your Septic tank working, Book a service today.

```html
<!DOCTYPE html>
<html lang="en">
<head>
<meta charset="utf-8">
<title>BRDQ – Service Your Septic</title>
<link rel="stylesheet" href="https://fonts.googleapis.com/css2?family=Bubblegum+Sans&family=Oswald:wght@700&display=block">
<style>
  :root {
    --sky: #12f0ff;
    --ray-light: #e6d3c8;
    --ray-dark: #a4958d;
    --burst: #43e43c;
    --headline-red: #f4232c;
    --headline-cyan: #86dde8;
    --ink: #1d1a18;
    --phone-brown: #4a3026;
    --chevron: #e2231a;
    --paper: #ffffff;
    --slide-green: #5ed13a;
    --slide-water: #3fd8f0;
  }
  * { box-sizing: border-box; margin: 0; padding: 0; }
  html, body { width: 1200px; height: 628px; overflow: hidden; background: var(--paper); }
  .ad {
    position: relative;
    width: 1200px;
    height: 628px;
    background: var(--paper);
    overflow: hidden;
  }
  .backdrop {
    position: absolute;
    left: 10px; top: 28px;
    width: 1180px; height: 572px;
  }
  .headline {
    position: absolute;
    left: 20px; top: 0;
    width: 570px;
    height: 500px;
    font-family: "Bubblegum Sans", "Comic Sans MS", sans-serif;
    font-weight: 400;
    line-height: 1;
  }
  .headline__line {
    position: absolute;
    left: 0; right: 0;
    text-align: center;
    white-space: nowrap;
  }
  .headline__line--lead {
    font-size: 76px;
    color: var(--headline-red);
    text-shadow: 3px 3px 0 var(--paper), -3px -3px 0 var(--paper), 3px -3px 0 var(--paper), -3px 3px 0 var(--paper), 0 3px 0 var(--paper), 3px 0 0 var(--paper), 0 -3px 0 var(--paper), -3px 0 0 var(--paper);
  }
  .headline__line--tail {
    font-size: 80px;
    color: var(--headline-cyan);
    text-shadow: 3px 3px 0 var(--ink), -3px -3px 0 var(--ink), 3px -3px 0 var(--ink), -3px 3px 0 var(--ink), 0 3px 0 var(--ink), 3px 0 0 var(--ink), 0 -3px 0 var(--ink), -3px 0 0 var(--ink);
  }
  .headline__line--1 { top: 56px; }
  .headline__line--2 { top: 154px; left: -20px; }
  .headline__line--3 { top: 278px; }
  .headline__line--4 { top: 384px; left: 0; }
  .phone {
    position: absolute;
    left: 44px; top: 516px;
    display: flex;
    align-items: center;
    gap: 14px;
  }
  .phone__icon { width: 54px; height: 50px; }
  .phone__number {
    font-family: "Oswald", sans-serif;
    font-weight: 700;
    font-size: 66px;
    letter-spacing: 1px;
    color: var(--phone-brown);
    line-height: 1;
  }
  .slide-scene {
    position: absolute;
    left: 545px; top: 28px;
    width: 420px; height: 572px;
    background: linear-gradient(160deg, var(--slide-green) 0%, #7fbf4a 35%, var(--slide-water) 75%, #1fb8d8 100%);
    border-radius: 180px 40px 120px 60px;
  }
  .brand {
    position: absolute;
    right: 10px; bottom: 28px;
    width: 278px; height: 70px;
    background: var(--paper);
    display: flex;
    align-items: center;
    justify-content: center;
    gap: 18px;
  }
  .brand__name {
    font-family: "Oswald", sans-serif;
    font-weight: 700;
    font-size: 44px;
    color: var(--ink);
    line-height: 1;
  }
  .brand__dot {
    width: 44px; height: 44px;
    border-radius: 50%;
    background: #6f8fd0;
  }
</style>
</head>
<body>
<main class="ad">
  <svg class="backdrop" viewBox="0 0 1180 572" aria-hidden="true">
    <rect width="1180" height="572" fill="var(--sky)"/>
    <g class="rays">
      <polygon points="700,290 420,0 560,0" fill="var(--ray-light)"/>
      <polygon points="700,290 0,110 0,220" fill="var(--ray-light)"/>
      <polygon points="700,290 0,420 0,540" fill="var(--ray-light)"/>
      <polygon points="700,290 250,572 400,572" fill="var(--ray-light)"/>
      <polygon points="700,290 870,0 940,0" fill="var(--ray-dark)"/>
      <polygon points="700,290 1180,40 1180,110" fill="var(--ray-dark)"/>
      <polygon points="700,290 1180,240 1180,300" fill="var(--ray-dark)"/>
      <polygon points="700,290 1180,440 1180,520" fill="var(--ray-dark)"/>
      <polygon points="700,290 1040,572 1120,572" fill="var(--ray-dark)"/>
      <polygon points="700,290 1060,0 1130,0" fill="var(--ray-dark)"/>
    </g>
    <g class="speed-lines" stroke="var(--ink)" stroke-width="2">
      <line x1="30" y1="40" x2="120" y2="80"/>
      <line x1="10" y1="300" x2="90" y2="305"/>
      <line x1="40" y1="470" x2="120" y2="440"/>
      <line x1="1140" y1="60" x2="1060" y2="110"/>
      <line x1="1170" y1="200" x2="1080" y2="215"/>
      <line x1="1150" y1="380" x2="1070" y2="360"/>
      <line x1="980" y1="20" x2="950" y2="70"/>
    </g>
    <polygon class="burst" fill="var(--burst)"
      points="330,10 380,90 470,20 470,120 590,70 540,170 640,190 560,250 660,320 560,350 620,440 520,430 540,540 440,480 400,572 330,500 250,572 220,480 120,540 130,430 20,450 90,350 0,300 90,250 10,180 120,160 80,60 190,110 200,10 270,80"/>
  </svg>

  <h1 class="headline">
    <span class="headline__line headline__line--lead headline__line--1">Service Your</span>
    <span class="headline__line headline__line--lead headline__line--2">Septic</span>
    <span class="headline__line headline__line--tail headline__line--3">and let the fun</span>
    <span class="headline__line headline__line--tail headline__line--4">Begin</span>
  </h1>

  <div class="phone">
    <svg class="phone__icon" viewBox="0 0 54 50" aria-hidden="true">
      <polyline points="4,6 22,25 4,44" fill="none" stroke="var(--chevron)" stroke-width="7"/>
      <polyline points="26,6 44,25 26,44" fill="none" stroke="var(--chevron)" stroke-width="7"/>
    </svg>
    <span class="phone__number">0400 555 123</span>
  </div>

  <div class="slide-scene" role="img" aria-label="Cartoon of three cheerful poo characters riding down a green water slide toward a septic tank"></div>

  <div class="brand">
    <span class="brand__name">BRDQ</span>
    <span class="brand__dot"></span>
  </div>
</main>
</body>
</html>
```